Frozen Yoghurt
Aufgabenstellung
Es soll eine Postkarte erstellt werden
auf die Vorteile des Produkts dargestellt werden
- kein fett (98% fettfrei)
- keine künstlichen süssungsmittel
- low calorien
- Viel Calcium
- Viel Eiweiss
- Vitamine durch Frucht topping
Die Postkarte soll gleichzeitig dazu dienen dass man sie mit zu uns ins Geschäft bringt und dann ein gratis Muster bekommt.
Mitbewerber: www.plumdrizzle.com, www.velvocup.com

```html
<!DOCTYPE html>
<html lang="de">
<head>
<meta charset="utf-8">
<title>Frozen Yoghurt – Flyer und Gutscheinkarte</title>
<link rel="stylesheet" href="https://fonts.googleapis.com/css2?family=Courgette&display=swap">
<style>
  :root {
    --stage: #7a141e;
    --card-deep: #8c1a24;
    --card-mid: #b5343a;
    --card-light: #e0857f;
    --glow: #fbe9e4;
    --ink: #ffffff;
    --line: rgba(255,255,255,0.85);
  }
  * { margin: 0; padding: 0; box-sizing: border-box; }
  html, body { width: 1200px; height: 703px; overflow: hidden; background: var(--stage); }
  body { position: relative; font-family: "Courgette", cursive; color: var(--ink); }

  .flyer {
    position: absolute; left: 0; top: 12px; width: 490px; height: 682px; overflow: hidden;
    background: radial-gradient(ellipse 80% 60% at 35% 62%, var(--card-light) 0%, var(--card-mid) 45%, var(--card-deep) 100%);
  }
  .flyer__divider { position: absolute; inset: 0; }
  .flyer__title {
    position: absolute; left: 60px; top: 52px; font-size: 54px; font-weight: 400; line-height: 0.82;
    transform: rotate(-8deg); transform-origin: left top;
  }
  .flyer__title span { display: block; }
  .flyer__title .second { padding-left: 12px; }
  .flyer__claim {
    position: absolute; left: 184px; top: 150px; font-size: 12px; white-space: nowrap;
    transform: rotate(-15deg); transform-origin: left top;
  }
  .flyer__slogan {
    position: absolute; left: 158px; top: 262px; font-size: 27px; white-space: nowrap;
    transform: rotate(-15deg); transform-origin: left top;
  }
  .flyer__photo {
    position: absolute; left: 180px; top: 320px; width: 320px; height: 340px;
    background: radial-gradient(ellipse 50% 48% at 52% 55%, var(--glow) 0%, #f1c3b8 40%, rgba(200,70,80,0.5) 72%, rgba(180,52,58,0) 100%);
  }

  .postcard {
    position: absolute; left: 511px; top: 111px; width: 680px; height: 483px;
    background: radial-gradient(ellipse 70% 75% at 28% 55%, var(--card-light) 0%, var(--card-mid) 45%, var(--card-deep) 100%);
  }
  .postcard__title {
    position: absolute; left: 35px; top: 44px; font-size: 54px; font-weight: 400; line-height: 0.82;
    transform: rotate(-8deg); transform-origin: left top;
  }
  .postcard__title span { display: block; }
  .postcard__title .second { padding-left: 12px; }
  .benefits {
    position: absolute; left: 60px; top: 225px; width: 230px; list-style: none;
    transform: rotate(-12deg); transform-origin: left top; font-size: 15px;
  }
  .benefits li { padding: 7px 0 9px; border-bottom: 1.5px dashed var(--line); white-space: nowrap; }
  .benefits li:last-child { border-bottom: none; }
  .benefits li:nth-child(n+2) { margin-left: 6px; }
  .postcard__rule { position: absolute; left: 395px; top: 24px; width: 1px; height: 433px; background: var(--line); }
  .voucher {
    position: absolute; left: 452px; top: 152px; font-size: 16px; line-height: 1.4; white-space: nowrap;
    transform: rotate(-15deg); transform-origin: left top;
  }
  .voucher .highlight { font-size: 21px; }
  .address-form { position: absolute; left: 423px; top: 282px; width: 230px; }
  .address-form .field { border-top: 1px solid var(--line); height: 43px; padding-top: 4px; font-size: 7px; }
</style>
</head>
<body>
  <section class="flyer">
    <svg class="flyer__divider" width="490" height="682" viewBox="0 0 490 682" aria-hidden="true">
      <line x1="0" y1="273" x2="490" y2="140" stroke="#fff" stroke-width="2"/>
    </svg>
    <h1 class="flyer__title"><span>frozen</span><span class="second">yoghurt</span></h1>
    <p class="flyer__claim">nordic bowl: makes you feel good</p>
    <p class="flyer__slogan">dein mund ist mein ziel</p>
    <div class="flyer__photo" role="img" aria-label="Foto: Becher mit Frozen Yoghurt, Kirschen und Müsli-Topping"></div>
  </section>

  <section class="postcard">
    <h2 class="postcard__title"><span>frozen</span><span class="second">yoghurt</span></h2>
    <ul class="benefits">
      <li>kein fett (98% fettfrei)</li>
      <li>keine künstlichen süssungsmittel</li>
      <li>low calorien</li>
      <li>viel calcium</li>
      <li>viel eiweiss</li>
      <li>vitamine durch frucht topping</li>
    </ul>
    <div class="postcard__rule"></div>
    <p class="voucher">gutschein für einen <span class="highlight">gratis</span><br>frozen yoghurt</p>
    <div class="address-form">
      <div class="field">name vorname</div>
      <div class="field">straße hausnummer</div>
      <div class="field">plz ort</div>
      <div class="field">email adresse</div>
    </div>
  </section>
</body>
</html>
```